Electrical Industry Newletter Design Project PSD format with layers

The Name of the newsletter is:
A "Pulse" in the Ages
-This is a bi monthly newsletter focused on the Electrical and Cabling Industry
"Pulse" of course is a play on words referring to a Sine wave
We are looking for a creative yet professional looking newsletter. Our targeted audience are professional consulting engineers, architects, & property owners/manager.
We are looking for a unique logo for the newsletters name "Pulse in the Ages" with the subtext being "Electrical & Cabling Industry"
We envision the incorporations of the sin wave into the logo and other such associated symbols associated with our industry.
Note: the Newsletter is going to be brought to them by our company KAV Electric. Our logo should be incorporated near the top of the newsletter but be less prominent.
Each issue is going to be a "Vol" Hence the Vol number should be editable.
There should be a featured article area labeled
-Whats Happening
-This section should have a spot for a relevant pictures
There should be a side section labeled
-Code Alert!
-Just for laughs
-This section should be available to place a relevant picture or comic strips of sorts.
The should be a section labeled
-Project Profile (This will be where we profile a recent project with pictures
You have total artistic license with this project, I know you will produce a great work of art!
Updates
Target Market(s)
Consulting Engineers, Architects, Specifiers, Building Owners & Managers
Industry/Entity Type
Electrical
Look and feel
Each slider illustrates characteristics of the customer's brand and the style your logo design should communicate.

```html
<!DOCTYPE html>
<html lang="en">
<head>
<meta charset="utf-8">
<title>A "Pulse" in the Ages – Newsletter Vol 01</title>
<link rel="stylesheet" href="https://fonts.googleapis.com/css2?family=PT+Sans:ital,wght@0,400;0,700;1,400;1,700&display=swap">
<style>
:root{
  --yellow:#f5b800;
  --charcoal:#3a3b3d;
  --ink:#2b2b2b;
  --red:#ec2227;
  --white:#ffffff;
  --paper:#f4f4f4;
  --night:#1c2631;
  --footer:#111111;
  --body-light:#e6e6e6;
}
*{margin:0;padding:0;box-sizing:border-box}
html,body{width:1200px;height:3309px;overflow:hidden;background:var(--white)}
body{font-family:"PT Sans",Arial,sans-serif;color:var(--ink)}
.canvas{position:relative;width:1200px;height:3309px;overflow:hidden;background:var(--white)}
.abs{position:absolute}

/* Masthead */
.masthead-title{left:60px;top:42px;font-weight:700;font-style:italic;color:var(--ink);line-height:1}
.masthead-title .name{font-size:46px;display:block;letter-spacing:.5px}
.masthead-title .word{font-size:54px;display:block;letter-spacing:1px}
.masthead-tagline{left:58px;top:150px;font-size:25px;font-weight:700;font-style:italic;color:var(--yellow);letter-spacing:1px}
.vol-badge{left:600px;top:0;width:122px;height:137px;background:var(--yellow);color:var(--white);text-align:center;font-weight:700;line-height:1}
.vol-badge .vol{display:block;font-size:26px;padding-top:10px}
.vol-badge .num{display:block;font-size:46px}
.vol-badge .date{display:block;font-size:15px;margin-top:6px}
.sponsor-label{left:1010px;top:30px;font-size:17px;color:var(--ink)}
.sponsor-name{left:830px;top:56px;font-size:30px;font-weight:700;color:var(--ink);display:flex;align-items:center;gap:12px;letter-spacing:.5px}
.sponsor-name .mark{width:26px;height:26px;background:var(--yellow)}

/* Featured photos */
.photo{top:830px;height:478px}
.photo-cables{left:0;width:335px;background:linear-gradient(135deg,#f3f1ea 0%,#d9cfb3 45%,#5a4f3a 100%)}
.photo-pylon{left:335px;width:400px;background:linear-gradient(180deg,#6d8fb8 0%,#9fb9d6 55%,#c9d6e3 100%)}
.photo-warehouse{left:735px;width:465px;background:linear-gradient(160deg,#bcd7ef 0%,#4f7ca8 50%,#1f3a5c 100%)}
.band-svg{left:0;top:0}

/* What's happening */
.section-tab{background:var(--yellow);color:var(--ink);font-weight:700;text-transform:uppercase;display:flex;align-items:center;justify-content:center;box-shadow:0 4px 8px rgba(0,0,0,.35)}
.tab-happening{left:823px;top:254px;width:347px;height:95px;font-size:32px}
.happening-body{left:66px;top:386px;width:1082px;color:var(--body-light);font-size:17.5px;line-height:25px;text-align:justify}
.happening-body p{text-indent:20px}
.happening-body .hl{color:var(--yellow)}
.happening-body h3{color:var(--yellow);font-size:20px;margin-top:16px;line-height:24px}
.happening-body .pull{color:var(--yellow);font-style:italic;margin-top:22px}
.btn{background:var(--yellow);color:var(--ink);font-weight:700;text-transform:uppercase;display:flex;align-items:center;justify-content:center}
.btn-read{left:51px;top:818px;width:139px;height:62px;font-size:15px}
.tab-photos{left:909px;top:874px;width:254px;height:53px;font-size:19px}

/* Code alert */
.alert-block{left:0;top:1399px;width:238px;height:229px;background:var(--red);display:flex;align-items:center;justify-content:center}
.alert-text{left:276px;top:1392px;width:551px;font-size:18px;font-style:italic;line-height:25px;text-align:justify;color:var(--ink)}
.alert-circle{left:867px;top:1397px;width:264px;height:264px;border-radius:50%;background:var(--red);color:var(--white);font-weight:700;text-align:center;display:flex;flex-direction:column;justify-content:center;line-height:1}
.alert-circle .big{font-size:52px}
.alert-circle .small{font-size:38px}

/* Project section background */
.project-bg{left:0;top:2150px;width:1200px;height:1093px;background:linear-gradient(180deg,#2a3644 0%,#1a232e 45%,#2b3848 80%,#121a22 100%)}

/* Just for laughs */
.laughs-title{left:780px;top:1810px;font-size:40px;font-weight:700;color:var(--ink)}
.laughs-frame{left:113px;top:1882px;width:366px;height:287px;background:var(--white);border-radius:14px;padding:14px;box-shadow:0 10px 24px rgba(0,0,0,.25)}
.laughs-photo{width:100%;height:100%;background:linear-gradient(160deg,#f2f2f2 0%,#d8d8d8 60%,#aeb3ba 100%)}
.laughs-text{left:624px;top:1892px;width:523px;font-size:18px;line-height:25px;text-align:justify;color:var(--ink)}

/* Project profile */
.profile-title{left:0;top:2300px;width:1200px;text-align:center;color:var(--white);font-size:40px;font-weight:700}
.profile-sub{left:0;top:2382px;width:1200px;text-align:center;color:var(--white);font-size:19px;font-weight:700}
.project-img{width:402px;height:308px}
.img-pylon{left:199px;top:2493px;background:linear-gradient(180deg,#6b8fbd 0%,#a7c0dc 60%,#d3dee8 100%)}
.img-bench{left:600px;top:2806px;background:linear-gradient(135deg,#3c3c3c 0%,#8a8a8a 45%,#c9b8a4 100%)}
.project-card{width:402px;height:308px;background:var(--white);padding:34px 36px}
.card-1{left:600px;top:2493px}
.card-2{left:199px;top:2806px}
.project-card h4{font-size:22px;font-weight:700;margin-bottom:28px}
.project-card p{font-size:15.5px;line-height:20px;text-align:justify;text-indent:26px;color:var(--ink)}
.btn-vert{width:64px;height:160px;font-size:15px}
.btn-vert span{transform:rotate(90deg);white-space:nowrap}
.btn-vert-left span{transform:rotate(-90deg)}
.btn-p1{left:1004px;top:2563px}
.btn-p2{left:133px;top:2886px}

/* Footer */
.footer{left:0;top:3243px;width:1200px;height:66px;background:var(--footer);text-align:center;padding-top:10px}
.footer .contact{color:var(--yellow);font-size:15px;line-height:22px}
.footer .links{color:var(--white);font-size:13px;line-height:20px}
</style>
</head>
<body>
<div class="canvas">

  <!-- Masthead -->
  <div class="abs masthead-title"><span class="name">pulse in the ages</span><span class="word">NEWSLETTER</span></div>
  <div class="abs masthead-tagline">ELECTRICAL &amp; CABLING INDUSTRY</div>
  <div class="abs vol-badge"><span class="vol">VOL</span><span class="num">01</span><span class="date">MARCH<br>2017</span></div>
  <div class="abs sponsor-label">brought to you by</div>
  <div class="abs sponsor-name"><span class="mark"></span>KAV ELECTRIC LLC</div>

  <!-- Featured photos -->
  <div class="abs photo photo-cables" role="img" aria-label="Photo of network cables plugged into a patch panel"></div>
  <div class="abs photo photo-pylon" role="img" aria-label="Photo of a high-voltage transmission tower against the sky"></div>
  <div class="abs photo photo-warehouse" role="img" aria-label="Photo of a lit industrial warehouse interior with loading bays"></div>

  <!-- Dark feature band -->
  <svg class="abs band-svg" width="1200" height="940" viewBox="0 0 1200 940" aria-hidden="true">
    <polygon points="0,320 1200,188 1200,834 0,908" fill="var(--charcoal)"/>
    <polygon points="0,312 1200,180 1200,190 0,322" fill="var(--yellow)"/>
    <polygon points="0,900 1200,826 1200,838 0,912" fill="var(--yellow)"/>
  </svg>

  <div class="abs section-tab tab-happening">What's Happening</div>
  <div class="abs happening-body">
    <p>Lorem ipsum dolor sit amet, consectetur adipiscing elit. Donec id interdum ante, non vulputate elit. Aenean magna augue, ultricies vel condimentum vel, volutpat non urna. Phasellus tincidunt arcu porttitor massa aliquam ultrices. Integer condimentum in risus ut molestie. Vivamus at diam ornare ligula iaculis rutrum. Proin lacinia nisl eu pellentesque aliquet. Nam id elit sagittis, dapibus dui nec, vestibulum risus. Duis vel aliquam dui, vitae luctus est. Proin nibh est, euismod sit amet ornare sit amet, suscipit id erat. <span class="hl">Duis id sem eros.</span> Sed et dignissim ex.</p>
    <h3>HEADLINE</h3>
    <p>Nulla dignissim ornare eleifend. Curabitur in rhoncus tellus, a scelerisque enim. Pellentesque tempor consequat diam, nec sagittis nibh. Vivamus hendrerit scelerisque euismod. Etiam placerat tristique ligula, quis iaculis neque hendrerit pharetra. Integer sit amet nulla maximus, vulputate turpis rhoncus, condimentum ligula. Nulla quis rutrum quam. In hac habitasse platea dictumst.</p>
    <p class="pull">Sed eget ante et sem fringilla convallis vitae vel massa. Sed maximus faucibus metus, id eleifend arcu malesuada et. Praesent enim lacus, euismod sit amet dui non, feugiat viverra lectus. Sed quis augue arcu. Etiam sed suscipit urna, ac maximus elit. Praesent faucibus, nulla suscipit tempus egestas, lacus neque lobortis est, ac eleifend enim nibh sed eros. Lorem ipsum dolor sit amet, consectetur adipiscing elit.</p>
  </div>
  <div class="abs btn btn-read">Read More</div>
  <div class="abs section-tab tab-photos">Featured Photos</div>

  <!-- Code alert -->
  <div class="abs alert-block">
    <svg width="60" height="172" viewBox="0 0 60 172" aria-hidden="true">
      <polygon points="4,0 56,0 46,118 14,118" fill="var(--white)"/>
      <circle cx="30" cy="148" r="22" fill="var(--white)"/>
    </svg>
  </div>
  <div class="abs alert-text">
    Lorem ipsum dolor sit amet, consectetur adipiscing elit. Integer bibendum eros in diam aliquet, et commodo dolor venenatis. Nulla eleifend sapien sit amet odio imperdiet efficitur. Interdum et malesuada fames ac ante ipsum primis in faucibus. Cras eget massa lorem.<br>
    Quisque augue enim, pellentesque nec mi vitae, tincidunt gravida lectus. Cras facilisis varius iaculis. Nunc turpis tortor, blandit eget tristique et, dapibus sit amet dolor.<br>
    Nam at maximus tellus. In hac habitasse platea dictumst. Sed maximus eget leo ac vulputate. Morbi hendrerit mauris et nunc varius, vitae aliquet eros dictum.
  </div>
  <div class="abs alert-circle"><span class="big">CODE</span><span class="small">ALERT</span></div>

  <!-- Project background -->
  <div class="abs project-bg" role="img" aria-label="Dim photo of a warehouse loading dock with roller doors"></div>

  <!-- Just for laughs band -->
  <svg class="abs band-svg" style="top:1720px" width="1200" height="570" viewBox="0 1720 1200 570" aria-hidden="true">
    <polygon points="0,1842 1200,1732 1200,2272 0,2217" fill="var(--yellow)"/>
  </svg>
  <div class="abs laughs-title">JUST FOR LAUGHS</div>
  <div class="abs laughs-frame"><div class="laughs-photo" role="img" aria-label="Photo of a smiling man in a suit jacket"></div></div>
  <div class="abs laughs-text">
    Lorem ipsum dolor sit amet, consectetur adipiscing elit. Integer bibendum eros in diam aliquet, et commodo dolor venenatis. Nulla eleifend sapien sit amet odio imperdiet efficitur. Interdum et malesuada fames ac ante ipsum primis in faucibus. Cras eget massa lorem.<br>
    Quisque augue enim, pellentesque nec mi vitae, tincidunt gravida lectus. Cras facilisis varius iaculis. Nunc turpis tortor, blandit eget tristique et, dapibus sit amet dolor.<br>
    &nbsp;ullamcorper.<br>
    Morbi nec fringilla sem.
  </div>

  <!-- Project profile -->
  <div class="abs profile-title">PROJECT PROFILE</div>
  <div class="abs profile-sub">Lorem ipsum dolor sit amet, consectetur adipiscing elit.</div>

  <div class="abs project-img img-pylon" role="img" aria-label="Photo of a transmission tower and power lines"></div>
  <div class="abs project-card card-1">
    <h4>PROJECT 1</h4>
    <p>Lorem ipsum dolor sit amet, consectetur adipiscing elit. Aenean vestibulum ultricies lacus. Donec viverra lectus vitae pretium pulvinar. Vestibulum ut lacus pellentesque, commodo purus eu, semper ante.</p>
    <p>Curabitur dapibus iaculis ultricies. Vivamus pulvinar maximus libero at commodo. In hac habitasse platea dictumst.</p>
  </div>
  <div class="abs btn btn-vert btn-p1"><span>READ MORE</span></div>

  <div class="abs project-card card-2">
    <h4>PROJECT 2</h4>
    <p>Lorem ipsum dolor sit amet, consectetur adipiscing elit. Aenean vestibulum ultricies lacus. Donec viverra lectus vitae pretium pulvinar. Vestibulum ut lacus pellentesque, commodo purus eu, semper ante.</p>
    <p>Curabitur dapibus iaculis ultricies. Vivamus pulvinar maximus libero at commodo. In hac habitasse platea dictumst.</p>
  </div>
  <div class="abs project-img img-bench" role="img" aria-label="Photo of hands testing equipment with an oscilloscope"></div>
  <div class="abs btn btn-vert btn-vert-left btn-p2"><span>READ MORE</span></div>

  <!-- Footer -->
  <div class="abs footer">
    <div class="contact">KAV Electric, llc. 120 Harbor Lane Westbrook, New Jersey 07000 &nbsp;&nbsp;&nbsp; Phone: 555-014-2210 &nbsp;Fax: 555-014-2211 &nbsp;hello@kavelectric.example</div>
    <div class="links">Unsubscribe | &nbsp;Manage Email Preferences</div>
  </div>

</div>
</body>
</html>
```